HARBOUR LEDGER Insurance Business Card Design

We need a business card designed for our personal risk / life insurance business based in Sydney Australia called 'Harbour Ledger'.

We manage and implement life insurance policies for individuals, businesses and families. Work on estate planning and succession planning. We help individuals make sure that they will be covered financially in the event of disability or critical illness.

We would like to see designs that use the colours Black, Silver/Grey , White OR different shades of Blue that are suitable for the finance / professional industries.

The final design should communicate financial safety and can also feel contemporary.
Updates

Hello,

Thanks for submitting your design.
We have recieved MANY great new designs today, thank-you.
Sorry for the late notice but for legal reasons we must include additional information of the card as follows:

Level 5, Suite 5.08,
47 Wattlebury Lane
KELBRIDGE NSW 2093

Authorised Representative No. 418730
Tallowmere Wealth Partners Pty Ltd
ABN 47 608 215 934
AFS Licence No. 572904

PLEASE REMOVE:
S marcusfellowes

PLEASE ADD:
www.harbourledger.example

Industry/Entity Type

Life Insurance

Contact Information for Business Card

Marcus Fellowes
Senior Advisor
Managing Director

M +61400 572 918
E Marcus@harbourledger.example
S marcusfellowes

Level 5, Suite 5.08
47 Wattlebury Lane
KELBRIDGE NSW 2093

Font styles to use
Serif
Sans Serif

Requirements
Must have
• - LANDSCAPE design

- MUST BE DOUBLE SIDED

Level 5, Suite 5.08,
47 Wattlebury Lane
KELBRIDGE NSW 2093

ABN 47 608 215 934
AFS Licence No. 572904

PLEASE REMOVE:
S marcusfellowes

PLEASE ADD:
www.harbourledger.example
Nice to have
• - Can have a rounded corner... but doesn't have to

```html
<!DOCTYPE html>
<html lang="en">
<head>
<meta charset="utf-8">
<title>Harbour Ledger – Business Card</title>
<link href="https://fonts.googleapis.com/css2?family=Cinzel:wght@500&family=Arimo:wght@400;700&display=swap" rel="stylesheet">
<style>
  :root {
    --stage: #2e2e30;
    --card: #ffffff;
    --card-shade: #ececec;
    --ink: #2b2b2b;
    --ink-soft: #4a4a4a;
    --ink-muted: #6e6e6e;
    --rule: #8a8a8a;
    --band-light: #5c5c5e;
    --band-dark: #262626;
    --band-text: #ffffff;
  }
  * { box-sizing: border-box; margin: 0; padding: 0; }
  html, body { width: 1200px; height: 951px; overflow: hidden; }
  body {
    background: var(--stage);
    position: relative;
    font-family: "Arimo", Arial, sans-serif;
    color: var(--ink);
  }
  .card {
    position: absolute;
    width: 560px;
    height: 330px;
    border-radius: 18px;
    background: linear-gradient(160deg, var(--card) 55%, var(--card-shade));
    overflow: hidden;
  }
  .card--front { left: 110px; top: 90px; }
  .card--back  { left: 530px; top: 500px; }

  .brand {
    position: absolute;
    display: flex;
    align-items: center;
    gap: 14px;
  }
  .brand__mark { background: var(--ink); flex: none; }
  .brand__name {
    font-family: "Cinzel", Georgia, serif;
    font-weight: 500;
    color: var(--ink);
    letter-spacing: 0.5px;
    white-space: nowrap;
  }
  .card--front .brand { left: 52px; top: 110px; }
  .card--front .brand__mark { width: 50px; height: 50px; }
  .card--front .brand__name { font-size: 40px; }

  .card--back .brand { left: 38px; top: 38px; }
  .card--back .brand__mark { width: 38px; height: 38px; }
  .card--back .brand__name { font-size: 30px; }

  .legal {
    position: absolute;
    left: 116px;
    top: 184px;
    font-size: 11px;
    line-height: 15px;
    color: var(--ink-muted);
    list-style: none;
  }

  .band {
    position: absolute;
    left: 0; bottom: 0;
    width: 100%;
    height: 44px;
  }
  .band__url {
    position: absolute;
    bottom: 12px;
    font-size: 14px;
    color: var(--band-text);
    letter-spacing: 0.3px;
  }
  .card--front .band__url { left: 235px; }
  .card--back .band__url { right: 30px; }

  .rule {
    position: absolute;
    left: 38px; right: 30px;
    top: 156px;
    height: 1px;
    background: var(--rule);
  }
  .person {
    position: absolute;
    right: 30px;
    top: 136px;
    text-align: right;
  }
  .person__name { font-size: 17px; color: var(--ink-soft); }
  .person__role { font-size: 12px; font-weight: 700; margin-top: 8px; }

  .contact {
    position: absolute;
    left: 38px;
    top: 222px;
    list-style: none;
    font-size: 14px;
    line-height: 20px;
  }
  .contact li { display: flex; align-items: center; gap: 8px; }
  .contact svg { width: 12px; height: 12px; fill: var(--ink-soft); }

  .address {
    position: absolute;
    right: 30px;
    top: 214px;
    text-align: right;
    font-style: normal;
    font-size: 14px;
    line-height: 18px;
  }
</style>
</head>
<body>

  <section class="card card--front" aria-label="Card front">
    <div class="brand">
      <span class="brand__mark"></span>
      <span class="brand__name">HARBOUR LEDGER</span>
    </div>
    <ul class="legal">
      <li>Authorised Representative No. 418730</li>
      <li>Tallowmere Wealth Partners Pty Ltd</li>
      <li>ABN 47 608 215 934</li>
      <li>AFS Licence No. 572904</li>
    </ul>
    <svg class="band" viewBox="0 0 560 44" preserveAspectRatio="none" aria-hidden="true">
      <path d="M190 44 C205 44 205 6 225 6 L560 6 L560 44 Z" fill="var(--band-light)"/>
    </svg>
    <span class="band__url">www.harbourledger.example</span>
  </section>

  <section class="card card--back" aria-label="Card back">
    <div class="brand">
      <span class="brand__mark"></span>
      <span class="brand__name">HARBOUR LEDGER</span>
    </div>
    <div class="rule"></div>
    <div class="person">
      <p class="person__name">Marcus Fellowes</p>
      <p class="person__role">Senior Advisor Managing Director</p>
    </div>
    <ul class="contact">
      <li>
        <svg viewBox="0 0 12 12" aria-hidden="true"><rect x="3" y="0" width="6" height="12" rx="1.2"/><rect x="4" y="1.5" width="4" height="7" fill="#fff"/></svg>
        +61400 572 918
      </li>
      <li>
        <svg viewBox="0 0 12 12" aria-hidden="true"><rect x="0" y="2" width="12" height="8" rx="1"/><path d="M0.5 2.5 L6 7 L11.5 2.5" stroke="#fff" stroke-width="1.2" fill="none"/></svg>
        Marcus@harbourledger.example
      </li>
    </ul>
    <address class="address">
      Level 5, Suite 5.08,<br>
      47 Wattlebury Lane<br>
      KELBRIDGE NSW 2093
    </address>
    <svg class="band" viewBox="0 0 560 44" preserveAspectRatio="none" aria-hidden="true">
      <path d="M300 44 C315 44 315 6 335 6 L560 6 L560 44 Z" fill="var(--band-dark)"/>
    </svg>
    <span class="band__url">www.harbourledger.example</span>
  </section>

</body>
</html>
```